Events By Quellon

Weddings, Corporate, Special Events
Memorable Catering, Personalized Menus, Custom Layout & Designs
Professional Staff, Excellent Service
Our Mission is Turning YOUR Vision into a Reality

Dorrie Quellon, Principal Planner
ph. 202 555-0187 - fax 301-555-0142
Email - eventsbyquellon@mailhaven.net
Web - www.cateringbyquellon.net
cateringbyquellon@Instagram

Target Market(s)

All Brides, Corprate Business, Special Events

Industry/Entity Type

Hospitality

Contact Information for Business Card

clean but affective

Font styles to use
Serif
Sans Serif
Script

Colors

Designer to choose colors to be used in the design.

Requirements
Must have
• logo with tagline using colors that will enhance what
• some pictures of nice table scape, hors d'oevures, upscale foods......
Nice to have
• Event: Something that happens or is regarded as happening, an occurrence especially one of some importance.
Should not have
• Use Logo on both sides

```html
<!DOCTYPE html>
<html lang="en">
<head>
<meta charset="utf-8">
<title>Events By Quellon — Business Card</title>
<link rel="stylesheet" href="https://fonts.googleapis.com/css2?family=Cinzel:wght@400;500&family=PT+Sans:wght@400&family=Lato:wght@400&display=swap">
<style>
  :root {
    --backdrop: #3b3b3c;
    --teal: #17aab8;
    --teal-bright: #27b4c2;
    --stone: #7e7f81;
    --white: #ffffff;
    --card-dark: #232122;
    --muted: #a6a6a6;
    --rule-light: rgba(255,255,255,0.45);
    --rule-dark: #5a5a5a;
  }
  * { margin: 0; padding: 0; box-sizing: border-box; }
  html, body { width: 1200px; height: 802px; overflow: hidden; }
  body { background: var(--backdrop); position: relative; font-family: "PT Sans", sans-serif; }

  .card {
    position: absolute; top: 274px; width: 443px; height: 265px; overflow: hidden;
    box-shadow: 0 3px 8px rgba(0,0,0,0.45);
  }
  .card--front { left: 136px; background: var(--teal); color: var(--white); }
  .card--back { left: 624px; background: var(--card-dark); }

  .brand-ornament { position: absolute; left: 0; top: 0; }

  .contact { position: absolute; right: 22px; text-align: right; }
  .contact__name {
    position: absolute; right: 22px; top: 30px;
    font-family: "Cinzel", serif; font-size: 21px; font-weight: 500; letter-spacing: 0.3px; white-space: nowrap;
  }
  .contact__title { position: absolute; right: 22px; top: 50px; font-size: 13.5px; }
  .contact__list { position: absolute; right: 22px; top: 75px; list-style: none; text-align: right; font-size: 12.5px; line-height: 15.8px; }
  .contact__list li { display: flex; justify-content: flex-end; align-items: center; gap: 3px; white-space: nowrap; }
  .contact__list svg { width: 10px; height: 10px; flex: none; }
  .contact__rule { position: absolute; left: 244px; right: 22px; top: 153px; border-top: 1px solid var(--rule-light); }
  .services { position: absolute; right: 22px; top: 169px; list-style: none; text-align: right; font-size: 13px; line-height: 15.7px; white-space: nowrap; }
  .services .sep { padding: 0 3px; }

  .brand-ring { position: absolute; left: 194px; top: 40px; width: 56px; height: 56px; border: 3px solid var(--stone); border-radius: 50%; }
  .brand-name {
    position: absolute; left: 0; right: 0; top: 125px; text-align: center;
    font-family: "Cinzel", serif; font-size: 24px; font-weight: 500; color: var(--teal); letter-spacing: 0.5px;
  }
  .brand-tagline {
    position: absolute; left: 0; right: 0; top: 162px; text-align: center;
    font-family: "Cinzel", serif; font-size: 8px; color: var(--muted); letter-spacing: 0.4px;
  }
  .mission {
    position: absolute; left: 0; right: 0; top: 183px; text-align: center;
    font-family: "Lato", sans-serif; font-size: 11.5px; color: var(--muted); letter-spacing: 0.2px;
  }
  .social { position: absolute; left: 59px; right: 61px; top: 219px; display: flex; align-items: center; gap: 6px; }
  .social__rule { flex: 1; border-top: 1px solid var(--rule-dark); }
  .social__dot { width: 16px; height: 16px; border-radius: 50%; background: #2a6a9a; flex: none; }
  .social__handle { font-family: "Lato", sans-serif; font-size: 12.5px; color: var(--teal-bright); white-space: nowrap; }
</style>
</head>
<body>

<section class="card card--front">
  <svg class="brand-ornament" width="240" height="265" viewBox="0 0 240 265" role="img" aria-label="Large brand monogram ornament in grey and white">
    <rect x="0" y="0" width="240" height="265" fill="var(--teal)"/>
    <circle cx="30" cy="140" r="140" fill="var(--white)"/>
    <circle cx="30" cy="150" r="128" fill="var(--stone)"/>
    <path d="M0 265 L0 200 Q120 210 200 235 Q225 248 222 265 Z" fill="var(--stone)"/>
  </svg>

  <h1 class="contact__name">Dorrie Quellon</h1>
  <p class="contact__title">Principal Planner</p>
  <ul class="contact__list">
    <li>202 555-0187
      <svg viewBox="0 0 10 10"><path d="M1 4 Q5 0 9 4 L8 5 L6.5 4 L6.5 3 Q5 2.5 3.5 3 L3.5 4 L2 5 Z M2 6 H8 V9 H2 Z" fill="var(--white)"/></svg></li>
    <li>301-555-0142
      <svg viewBox="0 0 10 10"><rect x="2.5" y="1" width="5" height="3" fill="var(--white)"/><rect x="0.5" y="4" width="9" height="4" rx="1" fill="var(--white)"/><rect x="2.5" y="6.5" width="5" height="3" fill="var(--white)"/></svg></li>
    <li>eventsbyquellon@mailhaven.net
      <svg viewBox="0 0 10 10"><rect x="0.5" y="2" width="9" height="6.5" fill="var(--white)"/><path d="M0.5 2 L5 5.5 L9.5 2" stroke="var(--teal)" stroke-width="1" fill="none"/></svg></li>
    <li>www.cateringbyquellon.net
      <svg viewBox="0 0 10 10"><circle cx="5" cy="5" r="4.5" fill="var(--white)"/><path d="M5 0.5 V9.5 M0.5 5 H9.5" stroke="var(--teal)" stroke-width="0.8"/></svg></li>
  </ul>
  <div class="contact__rule"></div>
  <ul class="services">
    <li>Weddings <span class="sep">|</span> Professional Staff</li>
    <li>Special Events <span class="sep">|</span> Corporate</li>
    <li>Memorable Catering</li>
    <li>Personalized Menus and Designs</li>
  </ul>
</section>

<section class="card card--back">
  <div class="brand-ring"></div>
  <h2 class="brand-name">Events By Quellon</h2>
  <p class="brand-tagline">Events Designed with You in Mind</p>
  <p class="mission">OUR MISSION IS TURNING YOUR VISION INTO A REALITY</p>
  <div class="social">
    <span class="social__rule"></span>
    <span class="social__dot"></span>
    <span class="social__handle">cateringbyquellon@Instagram</span>
    <span class="social__rule"></span>
  </div>
</section>

</body>
</html>
```